Invitation for a charity event - Plum Falcon - 5 x 7 inches

This is an event held at Sol Vista Raceway in San Diego, California. This invitation can have any theme related to horseracing, the beach or even Lyle Pemberton, who was a founder of Sol Vista.

here is the content of the invitation:
Hold your horses....
Plum Falcon 21 will be here on August 22nd!

This fine event started as just a thought,
between the two great minds of "Plum" and "the Falcon."
They said, "Let's get 20 guys in a Sol Vista suite,"
with beer, Varenne Noir and plenty to eat.
21 years ago they made it happen,
When Walt started singing, toes would be tappin'
The ticket was so hot, there was a waiting list,
And for this spectacular event no one would miss.
Fast forward to the present and look how it's evolved.
How it got to epic status is a puzzle yet to be solved.
One things for certain and I can say this so loud,
ALL OF THE FALLEN FALCONS WOULD BE SO PROUD!

Thursday, August 22nd, 12:30 pm. Lunch served at 1:00
Sol Vista Raceway, Paddock Lounge Suite K
RSVP: Marla Quinby - marlaquinby47@postwell.example
(415) 555-0198
* Men, sports coat required

Target Market(s)

Men and women

Colors

Designer to choose colors to be used in the design.

Requirements
Must have
• All the content above must be included. Invitation should be 5 x 7 inches
• ***the logo I've included can be used in the invitation but doesn't have to be used. If it is used, please change the 20 to 21***** Thank you!

```html
<!DOCTYPE html>
<html lang="en">
<head>
<meta charset="utf-8">
<title>Plum Falcon 21 Invitation</title>
<link rel="stylesheet" href="https://fonts.googleapis.com/css2?family=Roboto:wght@700;900&family=Roboto+Condensed:wght@300;400;700&display=swap">
<style>
  :root {
    --ink: #111111;
    --panel: rgba(22, 22, 22, 0.94);
    --panel-rule: #b9b9b9;
    --paper-text: #f4f4f4;
    --meadow-light: #c9c49a;
    --meadow-mid: #a3a46e;
    --meadow-deep: #8c9460;
    --coat-dark: #2b211c;
    --coat-mid: #4a3a31;
  }
  html, body {
    margin: 0;
    padding: 0;
    width: 857px;
    height: 1200px;
    overflow: hidden;
    background: #ffffff;
  }
  .invitation {
    position: relative;
    width: 857px;
    height: 1200px;
    overflow: hidden;
    font-family: "Roboto Condensed", "Arial Narrow", sans-serif;
    color: var(--ink);
  }
  .hero-photo {
    position: absolute;
    inset: 0;
    background:
      radial-gradient(ellipse 250px 330px at 630px 500px, var(--coat-mid) 0%, var(--coat-dark) 60%, rgba(43,33,28,0) 100%),
      radial-gradient(ellipse 200px 640px at 40px 880px, var(--coat-dark) 0%, rgba(43,33,28,0) 100%),
      linear-gradient(180deg, var(--meadow-light) 0%, var(--meadow-mid) 50%, var(--meadow-deep) 100%);
  }
  .headline {
    position: absolute;
    top: 42px;
    left: 0;
    width: 857px;
    margin: 0;
    text-align: center;
    font-family: "Roboto", Arial, sans-serif;
    font-weight: 900;
    font-size: 72px;
    line-height: 1;
    letter-spacing: 0.5px;
  }
  .subhead {
    position: absolute;
    top: 121px;
    left: 0;
    width: 857px;
    margin: 0;
    text-align: center;
    font-family: "Roboto", Arial, sans-serif;
    font-weight: 700;
    font-size: 33px;
    line-height: 40px;
  }
  .subhead sup, .event-date sup { font-size: 0.55em; vertical-align: 0.7em; line-height: 0; }
  .poem-panel {
    position: absolute;
    left: 69px;
    top: 237px;
    width: 411px;
    height: 717px;
    background: var(--panel);
  }
  .poem-frame {
    position: absolute;
    left: 19px;
    top: 23px;
    width: 369px;
    height: 666px;
    border: 1px solid var(--panel-rule);
    box-sizing: border-box;
  }
  .poem {
    position: absolute;
    left: 52px;
    top: 52px;
    width: 324px;
    color: var(--paper-text);
    font-weight: 300;
    font-size: 23.5px;
    line-height: 28.6px;
  }
  .poem p { margin: 0 0 28.6px; }
  .details {
    position: absolute;
    left: 502px;
    top: 840px;
    width: 340px;
  }
  .event-date {
    margin: 0;
    font-weight: 700;
    font-size: 31px;
    line-height: 34px;
  }
  .event-time {
    margin: 0;
    font-weight: 700;
    font-size: 23.5px;
    line-height: 27px;
  }
  .details-rule {
    width: 318px;
    height: 0;
    border-top: 2px solid var(--ink);
    margin: 7px 0 14px;
  }
  .venue {
    margin: 0;
    font-weight: 700;
    font-size: 22px;
    line-height: 29px;
  }
  .rsvp-label {
    margin: 2px 0 0;
    font-weight: 700;
    font-size: 42px;
    line-height: 46px;
  }
  .rsvp-line {
    margin: 0;
    font-size: 22px;
    line-height: 29px;
    font-weight: 700;
  }
  .rsvp-line.email { font-weight: 400; }
  .event-mark {
    position: absolute;
    left: 192px;
    top: 1046px;
    display: flex;
    align-items: center;
    gap: 14px;
  }
  .event-mark-dot {
    width: 54px;
    height: 54px;
    border-radius: 50%;
    background: var(--ink);
  }
  .event-mark-name {
    font-weight: 700;
    font-size: 34px;
    line-height: 36px;
    color: var(--ink);
    text-align: center;
  }
</style>
</head>
<body>
<main class="invitation">
  <div class="hero-photo" role="img" aria-label="Close-up photograph of a dark bay horse in a bridle against a softly blurred green racetrack background"></div>

  <h1 class="headline">HOLD YOUR HORSES</h1>
  <p class="subhead">PLUM FALCON 21 WILL BE HERE<br>ON AUGUST 22<sup>ND</sup>!</p>

  <section class="poem-panel">
    <div class="poem-frame"></div>
    <div class="poem">
      <p>This fine event started as just a thought, between the two great minds of "Plum" and "the Falcon." They said, "Let's get 20 guys in a Sol Vista suite," with beer, Varenne Noir and plenty to eat.</p>
      <p>21 years ago they made it happen, When Walt started singing, toes would be tappin' The ticket was so hot, there was a waiting list, And for this spectacular event no one would miss. Fast forward to the present and look how it's evolved. How it got to epic status is a puzzle yet to be solved.</p>
      <p>One things for certain and I can say this so loud, ALL OF THE FALLEN FALCONS WOULD BE SO PROUD!</p>
    </div>
  </section>

  <section class="details">
    <p class="event-date">Thursday, August 22<sup>nd</sup>,</p>
    <p class="event-time">12:30 pm. Lunch served at 1:00</p>
    <div class="details-rule"></div>
    <p class="venue">Sol Vista Raceway,<br>Paddock Lounge Suite K</p>
    <p class="rsvp-label">RSVP:</p>
    <p class="rsvp-line">Marla Quinby</p>
    <p class="rsvp-line email">marlaquinby47@postwell.example</p>
    <p class="rsvp-line">(415) 555-0198</p>
    <p class="rsvp-line">* Men, sports coat required</p>
  </section>

  <div class="event-mark">
    <span class="event-mark-dot"></span>
    <span class="event-mark-name">PLUM FALCON<br>21</span>
  </div>
</main>
</body>
</html>
```